business stationery for email layout
startup company
Simple
RT
Via G. Morelli, 17
26813 Codogno LO
Italy
Info@Tallimora.com
www.tallimora.com
minimalist, retail, fashion, technology, internet, innovative,one-step ahead, easy, intuitive, immediate, serious,credible
logo blue version
logo grey version
symbol blue version
symbol grey version

```html
<!DOCTYPE html>
<html lang="it">
<head>
<meta charset="utf-8">
<title>Tallimora – Business Card</title>
<link rel="stylesheet" href="https://fonts.googleapis.com/css2?family=Open+Sans:wght@400;600;700&display=swap">
<style>
  :root {
    --navy: #1c3c8c;
    --royal: #2747b0;
    --cyan: #1aa7d6;
    --sky: #8fd3ee;
    --ink: #3a3a3a;
    --rule: #c9ccd2;
    --paper: #ffffff;
    --backdrop: #eceef1;
  }
  * { margin: 0; padding: 0; box-sizing: border-box; }
  html, body {
    width: 1200px; height: 780px; overflow: hidden;
    background: var(--backdrop);
    font-family: "Open Sans", Arial, sans-serif;
  }
  .card {
    position: absolute; left: 40px; top: 40px;
    width: 1120px; height: 700px;
    background: var(--paper);
    border-radius: 38px;
    overflow: hidden;
    box-shadow: 0 4px 18px rgba(0,0,0,0.12);
  }
  .brand-name {
    position: absolute; left: 150px; top: 150px;
    font-weight: 700; font-size: 112px; letter-spacing: -2px;
    color: var(--navy); line-height: 1;
  }
  .holder {
    position: absolute; right: 580px; top: 300px; text-align: right;
  }
  .holder-initials {
    font-weight: 700; font-size: 44px; color: var(--navy); line-height: 1;
    margin-bottom: 28px;
  }
  .holder-address {
    font-size: 23px; color: var(--ink); line-height: 1.45;
  }
  .divider {
    position: absolute; left: 570px; top: 290px;
    width: 2px; height: 200px; background: var(--rule);
  }
  .contacts {
    position: absolute; left: 600px; top: 285px;
    list-style: none;
  }
  .contacts li {
    display: flex; align-items: center; gap: 14px;
    font-size: 23px; color: var(--ink); height: 46px;
  }
  .contacts svg { width: 24px; height: 24px; flex: none; }
  .wave { position: absolute; left: 0; bottom: 0; width: 1120px; height: 220px; }
</style>
</head>
<body>
  <div class="card">
    <div class="brand-name">Tallimora</div>

    <div class="holder">
      <div class="holder-initials">RT</div>
      <div class="holder-address">Via G. Morelli, 17<br>26813 Codogno LO, Italy</div>
    </div>

    <div class="divider"></div>

    <ul class="contacts">
      <li>
        <svg viewBox="0 0 24 24"><path fill="var(--navy)" d="M6.6 10.8a15 15 0 0 0 6.6 6.6l2.2-2.2a1 1 0 0 1 1-.25 11.4 11.4 0 0 0 3.6.57 1 1 0 0 1 1 1V20a1 1 0 0 1-1 1A17 17 0 0 1 3 4a1 1 0 0 1 1-1h3.5a1 1 0 0 1 1 1c0 1.25.2 2.45.57 3.57a1 1 0 0 1-.25 1z"/></svg>
        +390271836402
      </li>
      <li>
        <svg viewBox="0 0 24 24"><path fill="var(--navy)" d="M7 3h10v5H7zM4 9h16a2 2 0 0 1 2 2v6h-4v4H6v-4H2v-6a2 2 0 0 1 2-2zm4 7v3h8v-3z"/></svg>
        +390271836459
      </li>
      <li>
        <svg viewBox="0 0 24 24"><circle cx="12" cy="12" r="9" fill="none" stroke="var(--navy)" stroke-width="2.4"/><circle cx="12" cy="12" r="3.4" fill="none" stroke="var(--navy)" stroke-width="2.4"/></svg>
        Info@Tallimora.com
      </li>
      <li>
        <svg viewBox="0 0 24 24" fill="none" stroke="var(--navy)" stroke-width="2"><circle cx="12" cy="12" r="9"/><ellipse cx="12" cy="12" rx="4" ry="9"/><path d="M3 12h18M5 7h14M5 17h14"/></svg>
        www.tallimora.com
      </li>
    </ul>

    <svg class="wave" viewBox="0 0 1120 220" preserveAspectRatio="none" aria-hidden="true">
      <defs>
        <linearGradient id="bandFill" x1="0" y1="0" x2="1" y2="0">
          <stop offset="0" stop-color="var(--royal)"/>
          <stop offset="0.5" stop-color="var(--navy)"/>
          <stop offset="1" stop-color="var(--royal)"/>
        </linearGradient>
      </defs>
      <path d="M0 70 C 300 90, 700 110, 1120 0 L1120 40 C 720 140, 320 120, 0 92 Z" fill="var(--sky)"/>
      <path d="M0 125 C 320 150, 720 160, 1120 40 L1120 220 L0 220 Z" fill="url(#bandFill)"/>
      <path d="M0 112 C 320 138, 720 150, 1120 30" fill="none" stroke="var(--cyan)" stroke-width="5"/>
    </svg>
  </div>
</body>
</html>
```